Design Project for Digital Recruitment Business

I am launching a new website in the Digital Marketing Recruitment space here in the UK.We are a start up so this very much phase 1 with our web offering.

Key points:

- I think it will be aproximately 5- 8 pages

- I am looking for wordpress(open on this)) design and coding/ development.

- It really is going to be a brochure site on the whole so don't expect any huge integration. I would like an RSS feed to publish our jobs on our site. I can get the code for that from my recruitment database partner Quillpost, all i will need is a blank page for that section?.Parley net,chirrup etc as well.

-I already have the logo.(See attached)which you guys delivered brilliantly on :-)

some reference sites I like the look of: http://www.orbitvale.example.co.uk http://www.ratchethouse.example.com/ http://www.webmavens.example.co.uk/

The menu bar on these sites are good, the language is good.I want contemporary and professional.It needs to connect to the viewer.
WE are in the social media space so that needs to fit/blend eg parleynet,GS.

SUGGESTED APPROACH
So I guess the best starting point would be to just submit a home page design so i can judge the styles I like best.Then the finalists of that round can submit another section of the website to see the consistency in terms of look and feel. I will then pick someone to work one on one with to complete the design and do the coding. That way no one gets to waste valuable time and energy :-)

Feel free to ping me questions
Updates

Reason: Hello All, I am going to extend by a few days. I have been inundated with work.However I Plan to look at all your designs this week end and respond to all your Queries. Thanks for your Patience.

Hi guys

here is a little more about us

We know that the career success of the candidates we place can have a great impact on the success of your business. We have built a network of talented industry professionals and an extensive knowledge of the market and its changing trends. We focus on career management,advice and consultancy.With over 30 years experience in our team we feel confident we can deliver. Our specialisms are Creative and Design,Digital Marketing,Editorial and Content,User Experience,and Technology related to building Websites.

In today's world of continually adapting,surviving and thriving we recognise that you rise and fall by the people you hire.That is why an expert  is required to help find those people in business critical roles. So if your online Marketing strategy is behind the times or your website traffic is poor for example we can help find people on a contract and permanent basis to bridge the gap in you marketing and E-commerce team. Pixel Scouts are specialists in these areas and offer a consultative approach to working with your business. If your business grows as a result of the people you recruited through us we could not be happier. Honest,straightforward,professional.

In terms of home page the Menu bar is 4-5 topics at most. 90% of the traffic to this website will be Candidates so Jobs will be the best content along with the 6 skill sets/categories and everything social after that.Very like Ratchet website I mentioned in the Brief. A couple of you are on the right tracks.
Hope this helps for now. I feel confident I can pick from one of you.

Kind regards

Martin

Soory one other thing,

RE; Images

People are tricky to do on Recruitment websites as its very PC and they dont look real enough.Animations of people are better in my humble opinion...

open to ideas/options

Thanks

Target Market(s)

marketeers,designers,ecommerce folks.

Industry/Entity Type

Business

Requirements
Must have
• open at this stage but obviously the logo design colours must sync with the overall look and feel.GS,chirrup,mingle+ must be dominant

```html
<!DOCTYPE html>
<html lang="en">
<head>
<meta charset="utf-8">
<title>Pixel Scouts – Talented People. Great Careers.</title>
<link rel="stylesheet" href="https://fonts.googleapis.com/css2?family=Dosis:wght@300;400;500;600&family=Noto+Serif:ital@1&family=Poppins:wght@600&family=Ubuntu:wght@500;700&display=swap">
<style>
  :root {
    --orange: #f05a00;
    --purple: #2f0b7c;
    --ink: #4a4a4a;
    --muted: #6b6b6b;
    --gold: #f6b800;
    --link: #2a8fd6;
    --hero-dark: #1c1d2a;
    --hero-mid: #4a4c5c;
    --nav-bg: #ececec;
    --line: #e3e3e3;
    --page: #ffffff;
    --footer-red: #b3261e;
  }
  * { box-sizing: border-box; margin: 0; padding: 0; }
  html, body { width: 955px; height: 1200px; overflow: hidden; background: var(--page); }
  body { position: relative; font-family: "Dosis", sans-serif; color: var(--ink); }

  .hero { position: absolute; left: 0; top: 0; width: 955px; height: 399px;
    background: radial-gradient(ellipse at 40% 50%, var(--hero-mid), var(--hero-dark) 75%); }
  .hero-portrait { position: absolute; left: 500px; top: 0; width: 455px; height: 399px;
    background: radial-gradient(ellipse at 50% 45%, #c89a82 0%, #8a6656 38%, rgba(40,38,50,0) 72%); }

  .site-nav { position: absolute; left: 111px; top: 31px; width: 727px; height: 59px;
    background: var(--nav-bg); display: flex; align-items: stretch; }
  .brand { display: flex; align-items: center; gap: 6px; width: 240px; padding-left: 8px; }
  .brand-dot { width: 26px; height: 26px; border-radius: 50%; background: var(--orange); }
  .brand-name { font-family: "Dosis", sans-serif; font-weight: 600; font-size: 26px; color: var(--purple); letter-spacing: -0.3px; }
  .nav-list { display: flex; list-style: none; width: 487px; justify-content: space-between; }
  .nav-list li { font-family: "Ubuntu", sans-serif; font-weight: 700; font-size: 11px; color: #222; white-space: nowrap;
    display: flex; align-items: flex-end; padding: 0 11px 12px; }
  .nav-list li.is-active { background: var(--orange); color: #fff; }

  .hero-title { position: absolute; left: 118px; top: 134px; font-family: "Ubuntu", sans-serif; font-weight: 700;
    font-size: 33px; color: #fff; letter-spacing: -0.2px; white-space: nowrap; }
  .job-search { position: absolute; left: 122px; top: 198px; width: 262px; height: 36px; display: flex;
    border-radius: 4px; overflow: hidden; box-shadow: 0 1px 3px rgba(0,0,0,.5); }
  .job-search-field { flex: 1; background: #fff; font-size: 13px; color: #333; padding: 9px 11px; }
  .job-search-button { width: 54px; background: linear-gradient(#a9a9a9, #7d7d7d); display: flex; align-items: center; justify-content: center; }
  .hero-intro { position: absolute; left: 124px; top: 254px; font-size: 15px; line-height: 22px; color: var(--gold); white-space: nowrap; }

  .section-title { font-family: "Poppins", sans-serif; font-weight: 600; font-size: 31px; letter-spacing: -2px; line-height: 1; white-space: nowrap; }
  .section-title .first { color: var(--purple); }
  .section-title .second { color: var(--orange); }

  .feature { position: absolute; top: 422px; width: 200px; text-align: center; }
  .feature .section-title { height: 50px; }
  .feature-card { position: relative; margin-top: 15px; height: 254px; border-radius: 6px; background: #fff;
    box-shadow: 0 0 5px rgba(0,0,0,.12); }
  .feature-clip { position: absolute; left: 60px; top: -20px; }
  .feature-photo { position: absolute; left: 18px; top: 44px; width: 164px; height: 85px; border-radius: 6px; }
  .feature-text { position: absolute; left: 0; top: 141px; width: 200px; font-size: 13px; line-height: 19.3px; color: var(--muted); white-space: nowrap; }

  .meet-us { position: absolute; left: 115px; top: 770px; width: 440px; }
  .meet-us p { font-size: 12.6px; line-height: 19.5px; color: var(--muted); margin-top: 12px; white-space: nowrap; }
  .meet-us p + p { margin-top: 19px; }

  .social-feed { position: absolute; left: 628px; top: 770px; width: 210px; }
  .social-feed .section-title { display: flex; align-items: center; gap: 10px; }
  .feed-mark { width: 26px; height: 26px; border-radius: 50%; background: var(--orange); }
  .post { margin-top: 14px; font-family: "Noto Serif", serif; font-style: italic; font-size: 9.6px; line-height: 14px; color: #555; white-space: nowrap; }
  .post:first-of-type { margin-top: 12px; }
  .post a { color: var(--link); text-decoration: none; margin-left: 4px; }
  .post time { display: block; color: var(--orange); }

  .footer { position: absolute; left: 0; top: 1012px; width: 955px; border-top: 1px solid var(--line); }
  .footer-heading { font-family: "Poppins", sans-serif; font-weight: 600; font-size: 12px; color: #111; letter-spacing: .2px; }
  .footer-col { position: absolute; top: 18px; font-size: 12px; line-height: 16.5px; color: var(--muted); white-space: nowrap; }
  .contact { left: 111px; }
  .contact .country { color: var(--footer-red); font-weight: 500; margin-top: 8px; }
  .contact .company { color: #333; }
  .quick-links { left: 408px; }
  .quick-links ul { list-style: none; columns: 2; column-gap: 18px; width: 160px; margin-top: 8px; line-height: 18.5px; padding-left: 2px; }
  .connect { left: 695px; }
  .social-icons { display: flex; gap: 8px; margin-top: 8px; }
  .social-icons span { width: 22px; height: 22px; }

  .copyright { position: absolute; left: 0; top: 1159px; width: 955px; height: 41px; background: var(--orange);
    color: #fff; font-size: 9.5px; font-weight: 500; text-align: center; line-height: 34px; }
</style>
</head>
<body>
  <header class="hero">
    <div class="hero-portrait" role="img" aria-label="Portrait photo of a smiling professional on a dark backdrop"></div>
    <nav class="site-nav">
      <div class="brand"><span class="brand-dot"></span><span class="brand-name">pixelscouts</span></div>
      <ul class="nav-list">
        <li class="is-active">HOME</li><li>CLIENTS</li><li>CANDIDATES</li><li>JOBS</li><li>ABOUT US</li><li>RESOURCES</li><li>CONTACT</li>
      </ul>
    </nav>
    <h1 class="hero-title">Talented People. Great Careers.</h1>
    <div class="job-search">
      <div class="job-search-field">Search for your perfect job...</div>
      <div class="job-search-button">
        <svg width="24" height="24" viewBox="0 0 24 24"><circle cx="12" cy="12" r="11" fill="#5a5a5a"/><circle cx="11" cy="10.5" r="4" fill="none" stroke="#fff" stroke-width="2"/><line x1="14" y1="13.5" x2="17.5" y2="17" stroke="#fff" stroke-width="2.4" stroke-linecap="round"/></svg>
      </div>
    </div>
    <p class="hero-intro">Lorem Ipsum is simply dummy text of the printing and typesetting<br>industry. Lorem Ipsum has been the industry's standard dummy text ever since the 1968.</p>
  </header>

  <section class="feature" style="left:115px">
    <h2 class="section-title"><span class="first">dream</span><span class="second">jobs</span></h2>
    <div class="feature-card">
      <svg class="feature-clip" width="80" height="50" viewBox="0 0 80 50"><rect x="2" y="33" width="76" height="10" rx="5" fill="#fff" stroke="#cfcfcf"/><rect x="34" y="0" width="12" height="40" rx="4" fill="#e9e9e9" stroke="#cfcfcf"/></svg>
      <div class="feature-photo" role="img" aria-label="Photo of a person holding a handwritten sign about loving their job" style="background:linear-gradient(90deg,#6a2aa6,#d7a66e 45%,#d7a66e 60%,#6a2aa6)"></div>
      <p class="feature-text">Lorem Ipsum is simply dummy text<br>of the printing and<br>typesetting industry. Lorem Ipsum<br>has been the industry's standard<br>dummy text ever since the 1968.</p>
    </div>
  </section>

  <section class="feature" style="left:371px">
    <h2 class="section-title"><span class="first">dream</span><span class="second">hire</span></h2>
    <div class="feature-card">
      <svg class="feature-clip" width="80" height="50" viewBox="0 0 80 50"><rect x="2" y="33" width="76" height="10" rx="5" fill="#fff" stroke="#cfcfcf"/><rect x="34" y="0" width="12" height="40" rx="4" fill="#e9e9e9" stroke="#cfcfcf"/></svg>
      <div class="feature-photo" role="img" aria-label="Photo of business people shaking hands at a meeting" style="background:linear-gradient(90deg,#e9ecef,#c9b4a2 45%,#5b6b85 80%,#2e3440)"></div>
      <p class="feature-text">Lorem Ipsum is simply dummy text<br>of the printing and<br>typesetting industry. Lorem Ipsum<br>has been the industry's standard<br>dummy text ever since the 1968.</p>
    </div>
  </section>

  <section class="feature" style="left:627px">
    <h2 class="section-title"><span class="first">join</span><span class="second">us</span></h2>
    <div class="feature-card">
      <svg class="feature-clip" width="80" height="50" viewBox="0 0 80 50"><rect x="2" y="33" width="76" height="10" rx="5" fill="#fff" stroke="#cfcfcf"/><rect x="34" y="0" width="12" height="40" rx="4" fill="#e9e9e9" stroke="#cfcfcf"/></svg>
      <div class="feature-photo" role="img" aria-label="Photo of a team joining hands in a high five" style="background:linear-gradient(90deg,#cfe0ee,#d8c2b0 50%,#b8c8d6)"></div>
      <p class="feature-text">Lorem Ipsum is simply dummy text<br>of the printing and<br>typesetting industry. Lorem Ipsum<br>has been the industry's standard<br>dummy text ever since the 1968.</p>
    </div>
  </section>

  <section class="meet-us">
    <h2 class="section-title"><span class="first">meet</span><span class="second">us</span></h2>
    <p>Lorem Ipsum is simply dummy text of the printing and typesetting industry. Lorem Ipsum has<br>been the industry's standard dummy text ever since the 1896s, when an unknown printer took a<br>galley of type and scrambled it to make a type specimen book.</p>
    <p>It has survived not only five centuries, but also the leap into electronic typesetting, remaining<br>essentially unchanged. It was popularised in the 1896s with the release of Typeline sheets<br>containing Lorem Ipsum passages, and more recently with desktop publishing software<br>like Folio Layout including versions of Lorem Ipsum.</p>
  </section>

  <aside class="social-feed">
    <h2 class="section-title"><span><span class="first">from</span><span class="second">chirrup</span></span><span class="feed-mark"></span></h2>
    <p class="post">Lorem Ipsum is simply dummy text of the<br>printing and... <a>prly.example/QGSrKu</a><time>10 Oct</time></p>
    <p class="post">Lorem Ipsum is simply dummy text of the<br>printing and... <a>prly.example/QGSrKu</a><time>10 Oct</time></p>
    <p class="post">Lorem Ipsum is simply dummy text of the<br>printing and... <a>prly.example/QGSrKu</a><time>10 Oct</time></p>
  </aside>

  <footer class="footer">
    <div class="footer-col contact">
      <h3 class="footer-heading">CONTACT US</h3>
      <div class="country">COUNTRY NAME</div>
      <div class="company">Pixel Scouts</div>
      <div>Telephone : +44 (0)20 7946 0183</div>
      <div>Fax : +44 (0)20 7946 0184</div>
      <div>Email : info@pixelscouts.example.com</div>
    </div>
    <div class="footer-col quick-links">
      <h3 class="footer-heading">QUICK LINKS</h3>
      <ul><li>Home</li><li>Clients</li><li>Candidates</li><li>Jobs</li><li>About us</li><li>Resources</li><li>Contact</li></ul>
    </div>
    <div class="footer-col connect">
      <h3 class="footer-heading">CONNECT WITH US</h3>
      <div class="social-icons">
        <span style="background:var(--purple)"></span><span style="background:var(--orange)"></span><span style="background:var(--purple)"></span><span style="background:#444"></span><span style="background:var(--orange)"></span>
      </div>
    </div>
  </footer>

  <div class="copyright">Copyright © 2012 The Pixel Scouts.  All rights reserved.</div>
</body>
</html>
```